The graphic design project is to create a book cover and potentially an accompanying logo for a book called The Steady Compass: A Field Guide for Guiding Teams Through Shifting Ground. The title is a working title and may change slightly. The book presents 10 capabilities that organizational leaders should have to be able to lead in a world filled with uncertainties. The main themes are the following:• Leaders need to be clear and focused about the overall mission, but also need to make strategic decisions with a diversity of opinions and options.• Leaders must anticipate where they will need to adapt in implementing strategy.• Leaders need to create a culture that promotes trust and agility.• Leaders need to be vigilant and look for early indicators of change. Show intellectual curiosity.• Leaders should be willing to experiment and learn from the experiments.The book is designed as a handbook. This will be a self published business book.The below graphic provides what are the key concepts representing each letter of “COMPASSING”. The right-hand column provides key words / phrases associated with the concepts.

Target Market(s)

Mid to Senior level executives at global companies across industries.

Colors

Designer to choose colors to be used in the design.

Requirements
Must have
• No must haves.
Nice to have
• Wide open on the design.

```html
<!DOCTYPE html>
<html lang="en">
<head>
<meta charset="utf-8">
<title>The Steady Compass — Book Cover</title>
<link rel="stylesheet" href="https://fonts.googleapis.com/css2?family=EB+Garamond:ital,wght@0,400;0,500;1,400;1,500&display=swap">
<style>
  :root {
    --backdrop: #2b211c;
    --cover: #000000;
    --ink-white: #ffffff;
    --ink-rose: #f09a98;
    --red-bright: #ee2a26;
    --red-deep: #7a1a18;
    --rose-muted: #b25a5c;
    --brown: #7a4a3c;
    --dot: #d9d9d9;
  }
  * { margin: 0; padding: 0; box-sizing: border-box; }
  html, body {
    width: 1200px; height: 1200px; overflow: hidden;
    background: var(--backdrop);
  }
  .canvas {
    position: relative; width: 1200px; height: 1200px;
    display: flex; align-items: center; justify-content: center;
  }
  .cover {
    position: relative; width: 732px; height: 1100px;
    background: var(--cover); overflow: hidden;
    font-family: "EB Garamond", Georgia, serif;
    color: var(--ink-white);
  }
  .cover > * { position: absolute; left: 0; width: 100%; text-align: center; }
  .pattern-top {
    top: 0; height: 50px;
    background: linear-gradient(90deg, var(--rose-muted), var(--red-bright) 20%, var(--red-deep) 40%, var(--rose-muted) 60%, var(--red-bright) 80%, var(--red-deep));
  }
  .pattern-bottom { bottom: 0; height: 240px; }
  .rule { height: 6px; }
  .rule svg { display: block; width: 100%; height: 6px; }
  .rule-1 { top: 157px; }
  .rule-2 { top: 322px; }
  .rule-3 { top: 489px; }
  .rule-4 { top: 660px; }
  .title-article {
    top: 172px; font-style: italic; font-weight: 500;
    font-size: 56px; line-height: 1;
  }
  .title-line-1 {
    top: 248px; font-size: 62px; line-height: 1;
    letter-spacing: 0.62em; padding-left: 0.62em;
    color: var(--ink-rose);
  }
  .title-line-2 {
    top: 350px; font-size: 94px; line-height: 1; font-weight: 500;
    letter-spacing: 0.1em; padding-left: 0.1em;
  }
  .subtitle {
    top: 538px; font-size: 22px; line-height: 46px; font-weight: 500;
    letter-spacing: 0.26em; padding-left: 0.26em;
    color: var(--ink-rose);
  }
  .author-name {
    top: 697px; font-size: 46px; line-height: 1;
    letter-spacing: 0.2em; padding-left: 0.2em;
  }
  .author-role {
    top: 760px; font-size: 19px; line-height: 1;
    letter-spacing: 0.22em; padding-left: 0.22em;
  }
</style>
</head>
<body>
<div class="canvas">
  <div class="cover">
    <div class="pattern-top" role="img" aria-label="Decorative band of overlapping red and rose rounded shapes"></div>

    <div class="rule rule-1"><svg viewBox="0 0 732 6"><line x1="78" y1="3" x2="295" y2="3" stroke="var(--dot)" stroke-width="3" stroke-linecap="round" stroke-dasharray="0 17"/><line x1="437" y1="3" x2="654" y2="3" stroke="var(--dot)" stroke-width="3" stroke-linecap="round" stroke-dasharray="0 17"/></svg></div>
    <p class="title-article">the</p>
    <h1 class="title-line-1">STEADY</h1>
    <div class="rule rule-2"><svg viewBox="0 0 732 6"><line x1="82" y1="3" x2="654" y2="3" stroke="var(--dot)" stroke-width="3" stroke-linecap="round" stroke-dasharray="0 17.3"/></svg></div>
    <h2 class="title-line-2">COMPASS</h2>
    <div class="rule rule-3"><svg viewBox="0 0 732 6"><line x1="82" y1="3" x2="654" y2="3" stroke="var(--dot)" stroke-width="3" stroke-linecap="round" stroke-dasharray="0 17.3"/></svg></div>
    <p class="subtitle">A FIELD GUIDE FOR GUIDING TEAMS<br>THROUGH SHIFTING GROUND</p>
    <div class="rule rule-4"><svg viewBox="0 0 732 6"><line x1="82" y1="3" x2="654" y2="3" stroke="var(--dot)" stroke-width="3" stroke-linecap="round" stroke-dasharray="0 17.3"/></svg></div>
    <p class="author-name">AUTHOR NAME</p>
    <p class="author-role">POSITION, AUTHOR</p>

    <svg class="pattern-bottom" role="img" aria-label="Decorative cluster of overlapping red, rose and brown rounded squares and circles" viewBox="0 0 732 240" preserveAspectRatio="none">
      <defs>
        <linearGradient id="cluster" x1="0" y1="0" x2="1" y2="0">
          <stop offset="0" stop-color="#8a3a3a"/>
          <stop offset="0.3" stop-color="#7a3a32"/>
          <stop offset="0.55" stop-color="#c8282c"/>
          <stop offset="0.8" stop-color="#a85456"/>
          <stop offset="1" stop-color="#7a1a18"/>
        </linearGradient>
      </defs>
      <path d="M0 110 C60 60 140 20 230 50 C300 80 360 80 420 40 C480 0 560 0 620 20 C680 40 710 30 732 40 L732 240 L0 240 Z" fill="url(#cluster)"/>
    </svg>
  </div>
</div>
</body>
</html>
```